Business Card

Hello! We need a business card for a kid's ski shop in Vail, CO. During the Fall/Winter months, we are primarily a children's ski outfitter; however, we also carry many high end boutique items. Our age ranges are from Birth to about age 15. Our clientele come from all over the world. We would like a business card that is timeless, but fun considering we are a children's store. We have a large web presence and are really trying to brand our website www.TotTrailhub.com. Since we have such a tourist clientele, we try to remind them that they can shop 365 at our website. I have attached our new logos. Here is our store info:
PipTrek
418 W. Birch Ln., Suite F7
Vail, CO 81657
970-528-3094
www.TotTrailhub.com

```html
<!DOCTYPE html>
<html lang="en">
<head>
<meta charset="utf-8">
<title>PipTrek Business Card</title>
<link rel="stylesheet" href="https://fonts.googleapis.com/css2?family=Noto+Sans:wght@400;700;800&display=swap">
<style>
  :root {
    --backdrop: #e8e6e3;
    --card-white: #f6f6f6;
    --ridge-grey: #e4e4e4;
    --brand-red: #d3161d;
    --ridge-red: #c3121a;
    --paper-text: #ffffff;
    --shadow: rgba(0, 0, 0, 0.16);
  }
  * { margin: 0; padding: 0; box-sizing: border-box; }
  html, body {
    width: 1200px;
    height: 997px;
    overflow: hidden;
    background: var(--backdrop);
    font-family: "Noto Sans", Verdana, sans-serif;
  }
  .canvas {
    position: relative;
    width: 1200px;
    height: 997px;
  }
  .card {
    position: absolute;
    width: 580px;
    height: 332px;
    overflow: hidden;
    border-radius: 3px;
    box-shadow: 0 12px 28px var(--shadow);
  }
  .card--front {
    left: 150px;
    top: 120px;
    background: var(--card-white);
  }
  .card--back {
    left: 470px;
    top: 530px;
    background: var(--brand-red);
  }
  .ridge-art {
    position: absolute;
    left: -40px;
    right: -40px;
    top: 30px;
    height: 190px;
    border-radius: 50% 50% 0 0 / 60% 60% 0 0;
  }
  .card--front .ridge-art {
    background: linear-gradient(180deg, var(--card-white) 0%, var(--ridge-grey) 45%, var(--ridge-grey) 70%, var(--card-white) 100%);
  }
  .card--back .ridge-art {
    top: 20px;
    background: linear-gradient(180deg, var(--brand-red) 0%, var(--ridge-red) 40%, var(--ridge-red) 70%, var(--brand-red) 100%);
  }
  .brand {
    position: absolute;
    left: 0;
    right: 0;
    top: 128px;
    display: flex;
    justify-content: center;
    align-items: center;
    gap: 14px;
  }
  .brand__dot {
    width: 30px;
    height: 30px;
    border-radius: 50%;
    background: var(--brand-red);
  }
  .brand__name {
    font-weight: 800;
    font-size: 66px;
    letter-spacing: 0.5px;
    color: var(--brand-red);
    line-height: 1;
  }
  .contact {
    position: absolute;
    left: 0;
    right: 0;
    top: 100px;
    text-align: center;
    color: var(--paper-text);
  }
  .contact__lines {
    font-style: normal;
    font-weight: 400;
    font-size: 18px;
    line-height: 24px;
    letter-spacing: 0.5px;
  }
  .contact__web {
    display: block;
    margin-top: 26px;
    font-weight: 700;
    font-size: 25px;
    letter-spacing: 0.6px;
    color: var(--paper-text);
    text-decoration: none;
  }
</style>
</head>
<body>
  <main class="canvas">
    <section class="card card--front" aria-label="Business card front">
      <div class="ridge-art" role="img" aria-label="Faint grey mountain range silhouette across the card"></div>
      <div class="brand">
        <span class="brand__dot"></span>
        <h1 class="brand__name">PipTrek</h1>
      </div>
    </section>

    <section class="card card--back" aria-label="Business card back">
      <div class="ridge-art" role="img" aria-label="Darker red mountain range silhouette across the upper card"></div>
      <div class="contact">
        <address class="contact__lines">
          PipTrek<br>
          418 W. Birch Ln., Suite F7<br>
          Vail, CO 81657<br>
          970-528-3094
        </address>
        <a class="contact__web" href="#">www.TotTrailhub.com</a>
      </div>
    </section>
  </main>
</body>
</html>
```